Briefkopf und Visitenkarte für Kanzlei
Zielgruppe
Wir sind eine Kanzlei mit Sitz in Neuss und den Schwerpunkten im Arbeitsrecht und Strafrecht. Unser Rechtsanwalt Kerem Albayrak ist zugleich Fachanwalt für das Arbeitsrecht. Unsere Zielgruppe sind alle Menschen, die in diesen beiden Gebieten Rechtsberatung oder Vertretung suchen. Nähere Informationen über uns findet Ihr auf www.hovenrat-kanzlei.de
Aufgabenstellung
Was ich möchte:
- das Design sollte schlicht sein und nicht zu dick auftragen. Zu schlicht ist aber auch nicht gut, schlielich soll erkennbar sein, dass die Briefvorlage nicht von einem Laien ertellt wurde, sondern von einem Designer.
- Farbakzente wie marineblau und gold sind gewünscht, allerdings nicht zu übertrieben, weil das sonst vom Textinhalt ablenkt und zu viel Tinte verbraucht.
- Der Briefkopf sollte folgende Informationen anzeigen: Fachanwaltstitel, Anschrift, Kontaktmöglichkeiten wie Telefon, Fax, E-Mail und Webseite, Öffnungszeiten, Bankverbindung und Umsatzsteuer IDNr.
- Eine Kopfzeile oder Fußzeile mit dem Kanzleinamen - / Logo, die auch ab Seite 1. weitergeführt wird.
- Die Seitenzahl sollte ersichtlich sein.
- Die Endddatei sollte hinsichtlich der angegebenen Daten (wie bspw. Telefonnummer und Anschrift) leicht veränderbar sein (gewünscht sind word und rtf als Dateiformat)
- Die Schriftart für den Schriftzug Halls Of Falcons ist Trajan pro.
Was ich nicht möchte:
- Keine Wasserzeichen in der Mitte des Textes. Das lenkt von der Schrift ab.
- Die Enddatei sollte nicht groß sein (idealerweise unter 0,75 -1 mb), da wir unsere Schreiben oft per Mail versenden und der Anhang dadurch zu groß würde.

```html
<!DOCTYPE html>
<html lang="de">
<head>
<meta charset="utf-8">
<title>Kerem Albayrak – Geschäftsausstattung</title>
<link rel="stylesheet" href="https://fonts.googleapis.com/css2?family=Cinzel:wght@400;500&family=Arimo:wght@400;700&family=Tinos&display=swap">
<style>
:root{
  --bg:#b3b3b3;
  --navy:#24357c;
  --navy-soft:#8a90c8;
  --gold-dark:#b59a4c;
  --gold:#d8c27a;
  --gold-light:#efe2a6;
  --taupe:#8c7b6a;
  --ink:#222;
  --paper:#fff;
  --gold-grad:linear-gradient(90deg,#a89868 0%,#e9dc9c 30%,#b89a3e 55%,#efe0a4 75%,#c2a657 100%);
}
*{margin:0;padding:0;box-sizing:border-box}
html,body{width:1200px;height:1200px;overflow:hidden;background:var(--bg)}
body{position:relative;font-family:Arimo,Arial,sans-serif;color:var(--ink)}
.piece{position:absolute;background:var(--paper);box-shadow:5px 6px 6px rgba(0,0,0,.35);overflow:hidden}
.abs{position:absolute;white-space:nowrap}
.medal{position:absolute;border-radius:50%;background:radial-gradient(circle at 35% 30%,var(--gold-light) 0%,var(--gold) 45%,var(--gold-dark) 100%)}
.brand-name{font-family:Cinzel,serif;color:var(--navy);font-weight:400;transform:translateX(-50%);text-align:center}
.brand-title{color:var(--taupe);transform:translateX(-50%);letter-spacing:.02em}
.center{transform:translateX(-50%);text-align:center}
.partner-name{font-family:Cinzel,serif;color:var(--navy)}
.partner-sub{letter-spacing:.45em;color:var(--ink)}
.gold-bar{position:absolute;background:var(--gold-grad)}
.label{color:var(--navy)}

/* letterhead */
.letterhead{left:48px;top:56px;width:504px;height:712px}
.letterhead .info{left:370px;font-size:6.4px;line-height:9.6px}
.fold-mark{position:absolute;left:10px;width:13px;height:1px;background:#ccc}
.column-rule{position:absolute;left:356px;top:120px;width:1px;height:566px;background:var(--gold)}
.page-number{font-family:Tinos,serif;font-size:11px}

/* envelopes */
.envelope-back{left:593px;top:50px;width:557px;height:280px}
.envelope-front{left:593px;top:409px;width:557px;height:360px;background:transparent;box-shadow:none;overflow:visible}
.envelope-front .body{position:absolute;left:0;top:81px;width:557px;height:279px;background:var(--paper);box-shadow:5px 6px 6px rgba(0,0,0,.35)}
.flap{position:absolute;left:0;top:0}

/* business card */
.card-front{left:65px;top:864px;width:409px;height:265px}
.card-back{left:660px;top:861px;width:407px;height:264px;background:var(--navy)}
.contact{left:196px;font-size:12px;color:#333}
</style>
</head>
<body>

<!-- Letterhead -->
<section class="piece letterhead" aria-label="Briefbogen">
  <div class="medal" style="left:229px;top:17px;width:44px;height:44px"></div>
  <div class="abs brand-name" style="left:251px;top:63px;font-size:16px">Kerem Albayrak</div>
  <div class="abs brand-title" style="left:251px;top:84px;font-size:8.4px">FACHANWALT FÜR ARBEITSRECHT</div>

  <div class="abs" style="left:72px;top:121px;font-size:6px">RA Kerem Albayrak • Hafenstr. 22 • 41460 Neuss</div>

  <div class="fold-mark" style="top:239px"></div>
  <div class="fold-mark" style="top:356px;left:15px;width:22px"></div>
  <div class="fold-mark" style="top:478px"></div>

  <div class="column-rule"></div>

  <div class="abs info" style="top:119px;font-size:7.4px">Hafenstr. 22 <span class="label">•</span> 41460 Neuss</div>
  <div class="abs info" style="top:134px">
    <div class="label">Kontakt:</div>
    <div><span class="label">Tel:</span>&nbsp;&nbsp;&nbsp;&nbsp;&nbsp;&nbsp;&nbsp;+49 (0) 2131 / 48 70 210</div>
    <div><span class="label">Fax:</span>&nbsp;&nbsp;&nbsp;&nbsp;&nbsp;&nbsp;+49 (0) 2131 / 48 70 211</div>
    <div><span class="label">E-Mail:</span> ra.kaalbayrak@hovenrat-kanzlei.de</div>
    <div><span class="label">Web:</span>&nbsp;&nbsp;&nbsp;&nbsp;&nbsp;www.hovenrat-kanzlei.de</div>
  </div>
  <div class="abs info" style="top:196px">
    <div class="label">Öffnungszeiten:</div>
    <div>Montag bis Freitag</div>
    <div>8:30 Uhr bis 13:00 Uhr</div>
    <div>und 14:00 Uhr bis 17.00 Uhr</div>
  </div>
  <div class="abs info" style="top:244px">
    <div class="label">Bankverbindung:</div>
    <div>Kerem Albayrak</div>
    <div>IBAN: DEXX XXXX XXXX XXXX XXXX X</div>
    <div>BIC: XXXXXXXX</div>
    <div>Rheinufer Bank</div>
  </div>

  <div class="abs center" style="left:430px;top:614px;font-size:7.4px;line-height:10.5px">Grunder und Mitglied der<br>Anwaltskooperation:</div>
  <div class="medal" style="left:417px;top:638px;width:26px;height:26px"></div>
  <div class="abs partner-name center" style="left:430px;top:666px;font-size:11px">Halls Of Falcons</div>
  <div class="abs partner-sub center" style="left:432px;top:680px;font-size:5px">ANWALTSKOOPFATION</div>

  <div class="abs page-number" style="left:44px;top:673px">-1-</div>
  <div class="gold-bar" style="left:0;top:692px;width:504px;height:7px"></div>
</section>

<!-- Envelope, back -->
<section class="piece envelope-back" aria-label="Briefumschlag Rückseite">
  <svg class="flap" width="557" height="82" viewBox="0 0 557 82" aria-hidden="true">
    <path d="M0 0 H557 L533 68 Q528 79 516 79 H42 Q31 79 27 68 Z" fill="var(--navy)"/>
  </svg>
  <div class="medal" style="left:251px;top:12px;width:54px;height:54px"></div>
</section>

<!-- Envelope, front -->
<section class="piece envelope-front" aria-label="Briefumschlag Vorderseite">
  <svg class="flap" width="557" height="80" viewBox="0 0 557 80" aria-hidden="true">
    <path d="M0 79 L27 10 Q31 0 42 0 H516 Q528 0 533 10 L557 79 Z" fill="var(--navy)"/>
  </svg>
  <div class="medal" style="left:252px;top:13px;width:54px;height:54px"></div>
  <div class="body">
    <div class="medal" style="left:96px;top:13px;width:54px;height:54px"></div>
    <div class="abs brand-name" style="left:123px;top:69px;font-size:20px">Kerem Albayrak</div>
    <div class="abs brand-title" style="left:123px;top:96px;font-size:11px">FACHANWALT FÜR ARBEITSRECHT</div>
    <div class="abs center" style="left:122px;top:177px;font-size:7.4px;line-height:10.5px">Grunder und Mitglied der<br>Anwaltskooperation:</div>
    <div class="medal" style="left:109px;top:203px;width:26px;height:26px"></div>
    <div class="abs partner-name center" style="left:122px;top:231px;font-size:11px">Halls Of Falcons</div>
    <div class="abs partner-sub center" style="left:124px;top:245px;font-size:5px">ANWALTSKOOPFATION</div>
    <div class="gold-bar" style="left:0;top:259px;width:337px;height:7px"></div>
    <div class="abs" style="left:342px;top:255px;font-size:10px;letter-spacing:.04em;color:#333">Hafenstr. 22 <span class="label">•</span> 41460 Neuss</div>
    <div class="gold-bar" style="left:515px;top:259px;width:42px;height:7px"></div>
  </div>
</section>

<!-- Business card, front -->
<section class="piece card-front" aria-label="Visitenkarte Vorderseite">
  <div class="medal" style="left:177px;top:18px;width:54px;height:54px"></div>
  <div class="abs brand-name" style="left:204px;top:77px;font-size:19px">Kerem Albayrak</div>
  <div class="abs brand-title" style="left:204px;top:102px;font-size:11px">FACHANWALT FÜR ARBEITSRECHT</div>

  <div class="abs center" style="left:89px;top:140px;font-size:9.6px;line-height:14px">Grunder und Mitglied der<br>Anwaltskooperation:</div>
  <div class="medal" style="left:71px;top:172px;width:36px;height:36px"></div>
  <div class="abs partner-name center" style="left:89px;top:210px;font-size:14px">Halls Of Falcons</div>
  <div class="abs partner-sub center" style="left:91px;top:229px;font-size:6.6px">ANWALTSKOOPFATION</div>

  <div style="position:absolute;left:178px;top:145px;width:1px;height:90px;background:var(--gold)"></div>

  <div class="abs contact" style="top:141px">Hafenstr. 22 - 41460 Neuss</div>
  <div class="abs contact label" style="top:166px;color:var(--navy)">Kontakt:</div>
  <div class="abs contact" style="top:188px"><span class="label">Tel:</span>&nbsp;&nbsp;&nbsp;&nbsp;&nbsp;&nbsp;+49 (0) 2131 / 48 70 210</div>
  <div class="abs contact" style="top:205px"><span class="label">Fax:</span>&nbsp;&nbsp;&nbsp;&nbsp;&nbsp;+49 (0) 2131 / 48 70 211</div>
  <div class="abs contact" style="top:223px;font-size:10.4px"><span class="label">E-Mail:</span> ra.kaalbayrak@hovenrat-kanzlei.de</div>

  <svg style="position:absolute;left:0;top:242px" width="409" height="23" viewBox="0 0 409 23" aria-hidden="true">
    <defs>
      <linearGradient id="cardGold" x1="0" x2="1">
        <stop offset="0" stop-color="#a89868"/><stop offset=".35" stop-color="#efe2a6"/>
        <stop offset=".65" stop-color="#c2a657"/><stop offset="1" stop-color="#e9dc9c"/>
      </linearGradient>
    </defs>
    <rect x="0" y="0" width="244" height="1.5" fill="var(--gold)"/>
    <path d="M0 12 H232 L221 23 H0 Z" fill="var(--navy)"/>
    <path d="M245 0 H409 V23 H222 Z" fill="url(#cardGold)"/>
    <g transform="translate(268 12)" fill="none" stroke="#333" stroke-width="1">
      <circle r="6"/><ellipse rx="2.6" ry="6"/><line x1="-6" y1="0" x2="6" y2="0"/>
      <path d="M-5 -3 H5 M-5 3 H5"/>
    </g>
  </svg>
  <div class="abs" style="left:281px;top:246px;font-size:10.6px;font-weight:700;color:#333">www.hovenrat-kanzlei.de</div>
</section>

<!-- Business card, back -->
<section class="piece card-back" aria-label="Visitenkarte Rückseite">
  <div class="medal" style="left:172px;top:69px;width:64px;height:64px"></div>
  <div class="abs brand-name" style="left:204px;top:146px;font-size:29px;color:var(--navy-soft)">Halls Of Falcons</div>
  <div class="gold-bar" style="left:0;top:245px;width:407px;height:7px"></div>
</section>

</body>
</html>
```